Website Redesign

I am looking to have our website redone. We recently paid to have this done and are very unhappy with the results. We're looking to have a much more modern and clean feeling while GREATLY enhancing the user experience. We are very close to have a new logo designed as well as having some brand colors (Pantone 3005C). We want our site to have a human feel to it without focusing completely on our products. That being said, we need our products to play a more prominent role as our current site doesn't very clearly display what we do.
Our website: lumvaro-seating.com
Websites we like (overall feel): jorvex.com, daltonrigg.com
Websites we like (functionality): brimfold.com
I apologize, we are new to ArtQuorum. I am showing a budget of $500 for this project. I know we'd go beyond that. I do not believe that we'll be able to overhaul our website for $500. I apologize for any confusion.

```html
<!DOCTYPE html>
<html lang="en">
<head>
<meta charset="utf-8">
<title>Lumvaro Seating — Commercial Furniture</title>
<link rel="stylesheet" href="https://fonts.googleapis.com/css2?family=Questrial&family=Arimo&display=swap">
<style>
  :root {
    --brand-blue: #0a84c8;
    --ink: #1e1e1e;
    --white: #ffffff;
    --banner-black: #000000;
    --wheel-dark: #2b2b2b;
    --wheel-mid: #4a4a4a;
    --wheel-light: #8e8e8e;
    --pointer: #e0651d;
    --footer-top: #ececec;
    --footer-bottom: #d6d6d6;
    --footer-ink: #2a2a2a;
  }
  * { box-sizing: border-box; margin: 0; padding: 0; }
  html, body { width: 1200px; height: 833px; overflow: hidden; background: var(--white); }
  body { position: relative; font-family: "Questrial", sans-serif; color: var(--ink); }

  .top-bar { position: absolute; left: 0; top: 0; width: 1200px; height: 12px; background: var(--brand-blue); box-shadow: 0 2px 3px rgba(0,0,0,.25); }

  .brand { position: absolute; left: 130px; top: 92px; display: flex; align-items: center; gap: 10px; }
  .brand-dot { width: 14px; height: 14px; border-radius: 50%; background: var(--brand-blue); }
  .brand-name { font-size: 34px; color: var(--ink); letter-spacing: 1px; }

  .hero { position: absolute; left: 70px; top: 196px; width: 1060px; height: 292px; border-radius: 36px;
    background: linear-gradient(100deg, #000 0%, #000 78%, #2a2a2a 86%, #111 100%);
    box-shadow: 0 18px 22px -8px rgba(0,0,0,.45); overflow: hidden; }
  .hero-photo { position: absolute; left: 30px; top: 10px; width: 340px; height: 282px;
    background: radial-gradient(ellipse at 45% 55%, #d9d9d9 0%, #9a9a9a 35%, #1a1a1a 70%, #000 100%); }
  .hero-headline { position: absolute; left: 382px; top: 52px; color: var(--white); text-transform: uppercase; line-height: 1; }
  .hero-headline .small { display: block; font-size: 29px; letter-spacing: 1px; }
  .hero-headline .large { display: block; font-size: 58px; letter-spacing: 1px; }
  .hero-headline .l1 { margin-bottom: 8px; }
  .hero-headline .l2 { margin-bottom: 12px; }
  .hero-headline .l3 { margin-bottom: 10px; }
  .hero-nav { position: absolute; left: 790px; top: 44px; width: 200px; height: 200px; }

  .column { position: absolute; top: 540px; width: 410px; }
  .column.welcome { left: 145px; }
  .column.awesome { left: 647px; }
  .column h2 { color: var(--brand-blue); font-weight: 400; font-size: 30px; text-align: center; text-transform: uppercase; line-height: 40px; margin-bottom: 16px; letter-spacing: .5px; }
  .column p { font-size: 17px; line-height: 21.2px; text-align: justify; letter-spacing: 1px; color: var(--ink); }
  .column .more { display: block; text-align: right; margin-right: -18px; margin-top: -4px; font-size: 21px; color: var(--brand-blue); text-decoration: underline; line-height: 22px; }

  .site-footer { position: absolute; left: 0; top: 770px; width: 1200px; height: 63px;
    background: linear-gradient(var(--footer-top), var(--footer-bottom));
    font-family: "Arimo", Arial, sans-serif; font-size: 15px; color: var(--footer-ink); text-align: center; padding-top: 13px; line-height: 19px; }
</style>
</head>
<body>
  <div class="top-bar"></div>

  <header class="brand">
    <span class="brand-name">Lumvaro</span>
    <span class="brand-dot"></span>
  </header>

  <section class="hero">
    <div class="hero-photo" role="img" aria-label="Photo of a white sculpted commercial lounge chair on black"></div>
    <h1 class="hero-headline">
      <span class="small l1">We make comercial</span>
      <span class="large l2">Furniture</span>
      <span class="small l3">That’s inherently</span>
      <span class="large">Human</span>
    </h1>
    <svg class="hero-nav" viewBox="0 0 200 200" role="navigation" aria-label="Site sections">
      <defs>
        <path id="arc-top" d="M40,100 A60,60 0 0 1 160,100"/>
        <path id="arc-bottom" d="M34,100 A66,66 0 0 0 166,100"/>
      </defs>
      <circle cx="100" cy="100" r="91" fill="#1a1a1a" stroke="#6a6a6a" stroke-width="1.5"/>
      <g stroke="#111" stroke-width="2">
        <path d="M12,100 A88,88 0 0 1 100,12 L100,62 A38,38 0 0 0 62,100 Z" fill="var(--wheel-dark)"/>
        <path d="M100,12 A88,88 0 0 1 188,100 L138,100 A38,38 0 0 0 100,62 Z" fill="var(--wheel-light)"/>
        <path d="M188,100 A88,88 0 0 1 100,188 L100,138 A38,38 0 0 0 138,100 Z" fill="var(--wheel-mid)"/>
        <path d="M100,188 A88,88 0 0 1 12,100 L62,100 A38,38 0 0 0 100,138 Z" fill="var(--wheel-mid)"/>
      </g>
      <circle cx="100" cy="100" r="37" fill="#000"/>
      <g fill="#fff" font-family="Questrial, sans-serif" font-size="13" letter-spacing="1">
        <text><textPath href="#arc-top" startOffset="25%" text-anchor="middle">COMPANY</textPath></text>
        <text><textPath href="#arc-top" startOffset="75%" text-anchor="middle">PRODUCTS</textPath></text>
        <text><textPath href="#arc-bottom" startOffset="25%" text-anchor="middle">ORDERING</textPath></text>
        <text><textPath href="#arc-bottom" startOffset="75%" text-anchor="middle">CONTACT</textPath></text>
      </g>
      <path d="M14,36 L34,28 L28,50 Z" fill="var(--pointer)" stroke="#8a3a0a" stroke-width="1"/>
    </svg>
  </section>

  <section class="column welcome">
    <h2>Welcome to Lumvaro</h2>
    <p>Lorem ipsum dolor sit amet, consectetur adipisicing elit, sed do eiusmod tempor incididunt ut labore et dolore magna aliqua. Ut enim ad minim veniam, quis nostrud exercitation ullamco laboris nisi ut aliquip ex</p>
    <a class="more" href="#">more</a>
  </section>

  <section class="column awesome">
    <h2>What make us awesome?</h2>
    <p>Lorem ipsum dolor sit amet, consectetur adipisicing elit, sed do eiusmod tempor incididunt ut labore et dolore magna aliqua. Ut enim ad minim veniam, quis nostrud exercitation ullamco laboris nisi ut aliquip ex</p>
    <a class="more" href="#">more</a>
  </section>

  <footer class="site-footer">
    © 2013 Lumvaro Seating | 418 Corbel Lane, Suite 210, Fairhaven, OR 97304<br>
    Call Toll-free: 800.555.0193 | Fax: 555.201.4486 | Email Us
  </footer>
</body>
</html>
```